20 years in Business Magazine Ad

We need a half page advertisement, celebrating 20 years in business in 2016. We are a globalized Flavor and Fragrance Ingredient company called Velmoric Corp. I've attached a file of our current logos. I like the idea of the Globe with pearls- but we definitely need an updated version of it. Plus room for the website address, phone number and email address.

Industry/Entity Type

Business

Requirements
Must have
• Wording saying that we are celebrating 20 years in business
Nice to have
• Something that says to the reader that we are a global company

```html
<!DOCTYPE html>
<html lang="en">
<head>
<meta charset="utf-8">
<title>Velmoric Corp – 20 Years In Business</title>
<link rel="stylesheet" href="https://fonts.googleapis.com/css2?family=Jost:wght@400;700&family=Grand+Hotel&display=swap">
<style>
  :root {
    --stage: #3a3a3a;
    --paper: #f4f4f6;
    --pearl-light: #ffffff;
    --pearl-shade: #d9dade;
    --navy: #2b2f8c;
    --ink: #1c1c1c;
    --gold-light: #ffe58a;
    --gold: #f7c64a;
    --frame: #f3b43c;
  }
  * { box-sizing: border-box; margin: 0; padding: 0; }
  html, body {
    width: 1200px;
    height: 960px;
    overflow: hidden;
    background: var(--stage);
  }
  .ad {
    position: absolute;
    left: 0;
    top: 92px;
    width: 1200px;
    height: 776px;
    background: var(--paper);
    overflow: hidden;
    font-family: "Jost", Arial, sans-serif;
  }
  .ad__backdrop {
    position: absolute;
    inset: 0;
    background:
      radial-gradient(ellipse at 30% 70%, var(--pearl-light) 0%, transparent 55%),
      radial-gradient(ellipse at 75% 85%, var(--pearl-light) 0%, transparent 50%),
      linear-gradient(180deg, #f7f7f8 0%, #e9e9ec 45%, var(--pearl-shade) 100%);
  }
  .brand {
    position: absolute;
    left: 101px;
    top: 108px;
    display: flex;
    align-items: center;
    gap: 14px;
    color: var(--navy);
    font-size: 78px;
    font-weight: 400;
    line-height: 1;
  }
  .brand__dot {
    width: 26px;
    height: 26px;
    border-radius: 50%;
    background: var(--navy);
  }
  .website {
    position: absolute;
    right: 69px;
    top: 50px;
    color: var(--navy);
    font-size: 25px;
    letter-spacing: 0.3px;
  }
  .headline {
    position: absolute;
    left: 101px;
    top: 270px;
    color: var(--ink);
    font-family: "Grand Hotel", cursive;
    font-weight: 400;
    font-size: 96px;
    line-height: 1;
  }
  .headline__line { display: block; height: 112px; }
  .headline__line--years { height: 118px; color: var(--navy); }
  .headline__number {
    font-family: "Jost", Arial, sans-serif;
    font-weight: 700;
    font-size: 92px;
    letter-spacing: -2px;
    margin-right: 18px;
  }
  .feature-art {
    position: absolute;
    left: 796px;
    top: 243px;
    width: 331px;
    height: 381px;
    border: 12px solid var(--frame);
    background: radial-gradient(circle at 60% 40%, var(--gold-light) 0%, var(--gold) 100%);
  }
  .contact {
    position: absolute;
    right: 69px;
    top: 675px;
    text-align: right;
    color: var(--ink);
    font-size: 24px;
    line-height: 42px;
  }
  .contact__label { color: var(--navy); }
</style>
</head>
<body>
  <main class="ad">
    <div class="ad__backdrop" role="img" aria-label="Soft field of white pearls"></div>

    <div class="brand">
      <span class="brand__name">Velmoric</span>
      <span class="brand__dot"></span>
    </div>

    <p class="website">www.velmoriccorp.com</p>

    <h1 class="headline">
      <span class="headline__line">We Are</span>
      <span class="headline__line">Celebrating</span>
      <span class="headline__line headline__line--years"><span class="headline__number">20</span>Years</span>
      <span class="headline__line">In Business</span>
    </h1>

    <div class="feature-art" role="img" aria-label="Illustration of a woman holding up a globe wrapped in strings of pearls"></div>

    <div class="contact">
      <p><span class="contact__label">CALL US -</span> 1234 5678 90</p>
      <p><span class="contact__label">Email</span> - order@velmoriccorp.com</p>
    </div>
  </main>
</body>
</html>
```